Business card for our start up Automotive Shop

Clean business card design for our new automotive shop Harborline Motor Works. This card will be the template for all of our staff member including technicians and service advisors.

Harborline Motor Works is an automotive service shop catering to US domestic and asian import vehicles. We are a service and maintenance full service facility. Our aim is to provide the best quality workmanship and the best customer service experience in our industry.

Our target market are young professionals to people with families. We are not targeting a younger audience or the car modification scene. The card should be appealing to women of the 30+ age demographic.

We are a shop of younger professionals instead of an older crowd. The card design should reflect as such.

Target Market(s)

30+ Female demographic and 30+ male.

Industry/Entity Type

Automotive

Contact Information for Business Card

Must be clean and appealing to clients. Large enough and easy to read print.

Font styles to use
Sans Serif

Colors
f78f20
ffffff
b2b2b2
dddddd

Requirements
Must have
• Address, website and phone number
• 42-17 58th Ct
• Larkfield ME 04999
• (207) 555-0142
• harborlinemotorworks.example
• There must be an area to add a Name and e-mail address for personalization purposes.
Nice to have
• Back of the card should have website.
• I would also like to incorporate yelp, google+, Facebook, and instagram widgets. Will add the exact pages but everything can be @ or / harborlinemotorworks
• That can be added on the back of the card.

```html
<!DOCTYPE html>
<html lang="en">
<head>
<meta charset="utf-8">
<title>Harborline Motor Works — Business Cards</title>
<link href="https://fonts.googleapis.com/css2?family=Open+Sans:wght@400;600;700&display=swap" rel="stylesheet">
<style>
  :root {
    --orange: #f78f20;
    --white: #ffffff;
    --grey: #b2b2b2;
    --light-grey: #dddddd;
    --ink: #3a3a3a;
    --backdrop: #eeeae5;
  }
  * { box-sizing: border-box; margin: 0; padding: 0; }
  html, body { width: 1200px; height: 900px; overflow: hidden; }
  body {
    background: var(--backdrop);
    font-family: "Open Sans", Arial, sans-serif;
    position: relative;
  }
  .card {
    position: absolute;
    width: 560px;
    height: 320px;
    overflow: hidden;
    box-shadow: 0 10px 28px rgba(0,0,0,.18);
  }
  .card--back { left: 60px; top: 100px; background: var(--orange); color: var(--white); }
  .card--front { left: 580px; top: 480px; background: var(--white); color: var(--ink); }

  .faint-ring {
    position: absolute;
    border-radius: 50%;
    border: 46px solid;
  }
  .card--back .faint-ring { width: 330px; height: 330px; right: -40px; top: -20px; border-color: rgba(255,255,255,.12); }
  .card--front .faint-ring { width: 300px; height: 300px; right: -50px; top: 10px; border-color: rgba(178,178,178,.22); }

  .brand { position: absolute; display: flex; align-items: center; gap: 12px; }
  .brand__dot { width: 34px; height: 34px; border-radius: 50%; flex: none; }
  .brand__name { font-weight: 700; text-transform: uppercase; letter-spacing: 1.5px; white-space: nowrap; }
  .card--back .brand { left: 60px; top: 128px; }
  .card--back .brand__dot { background: var(--white); }
  .card--back .brand__name { font-size: 26px; color: var(--white); }
  .card--front .brand { left: 40px; top: 36px; }
  .card--front .brand__dot { background: var(--orange); }
  .card--front .brand__name { font-size: 24px; color: var(--orange); }

  .social { position: absolute; left: 0; right: 0; top: 215px; text-align: center; }
  .social__dots { display: flex; justify-content: center; gap: 10px; margin-left: 120px; }
  .social__dot { width: 22px; height: 22px; border-radius: 50%; background: var(--white); }
  .social__handle { margin: 10px 0 0 120px; font-size: 12px; font-weight: 600; }

  .person { position: absolute; left: 40px; top: 102px; }
  .person__name { font-size: 17px; font-weight: 700; color: var(--orange); text-transform: uppercase; letter-spacing: .3px; line-height: 22px; }
  .person__role { font-size: 14px; color: var(--ink); line-height: 20px; }

  .contact { position: absolute; left: 40px; top: 158px; list-style: none; }
  .contact__item { display: flex; align-items: center; gap: 10px; font-size: 15px; line-height: 23px; }
  .contact__icon { width: 13px; height: 13px; flex: none; }
  .address { position: absolute; left: 40px; top: 234px; font-size: 15px; line-height: 21px; font-style: normal; }

  .band { position: absolute; left: 0; top: 0; width: 560px; height: 320px; }
</style>
</head>
<body>

  <section class="card card--back" aria-label="Card back">
    <div class="faint-ring"></div>
    <div class="brand">
      <span class="brand__dot"></span>
      <span class="brand__name">Harborline Motor Works</span>
    </div>
    <div class="social">
      <div class="social__dots">
        <span class="social__dot"></span>
        <span class="social__dot"></span>
        <span class="social__dot"></span>
      </div>
      <p class="social__handle">@harborlinemotorworks</p>
    </div>
  </section>

  <section class="card card--front" aria-label="Card front">
    <div class="faint-ring"></div>
    <svg class="band" viewBox="0 0 560 320" aria-hidden="true">
      <polygon points="0,312 560,240 560,320 0,320" fill="var(--orange)"/>
      <polygon points="0,305 560,233 560,240 0,312" fill="var(--white)"/>
    </svg>
    <div class="brand">
      <span class="brand__dot"></span>
      <span class="brand__name">Harborline Motor Works</span>
    </div>
    <div class="person">
      <p class="person__name">Daniel Reyes</p>
      <p class="person__role">Managing Director</p>
    </div>
    <ul class="contact">
      <li class="contact__item">
        <svg class="contact__icon" viewBox="0 0 16 16"><path d="M3 1l3 3-1.5 2a9 9 0 0 0 5.5 5.5L12 10l3 3-2 2C7 15 1 9 1 3z" fill="var(--orange)"/></svg>
        (207) 555-0142
      </li>
      <li class="contact__item">
        <svg class="contact__icon" viewBox="0 0 16 16"><rect x="1" y="3" width="14" height="10" fill="var(--orange)"/><path d="M1 3l7 6 7-6" fill="none" stroke="var(--white)" stroke-width="1.4"/></svg>
        info@harborlinemotorworks.example
      </li>
      <li class="contact__item">
        <svg class="contact__icon" viewBox="0 0 16 16"><circle cx="8" cy="8" r="7" fill="var(--orange)"/><path d="M1 8h14M8 1c-3 4-3 10 0 14M8 1c3 4 3 10 0 14" fill="none" stroke="var(--white)" stroke-width="1"/></svg>
        www.harborlinemotorworks.example
      </li>
    </ul>
    <address class="address">42-17 58th Ct<br>Larkfield ME 04999</address>
  </section>

</body>
</html>
```